Business Card Design Project

Hello Designers, hope you are all aiming enjoy the weekend
I have the Business Logo (uploaded), you can alter the color which ever way you think would work,
Im looking for a simple yet striking feel, something which will stay memorable (I have uploaded 3 examples for you to flick through)
Information on the card, will just be the bare minimum,
Double Sided
Info being
i.e.
Name
Number
Website
ABN
Tobin Wexmoor
+468213579 (singapore)
+315792846 (Australia)
+729384615 (America)
www.lomevu-linkup.example
ABN 86420913
Enjoy,
Tobin
Industry/Entity Type
Business
Look and feel
Each slider illustrates characteristics of the customer's brand and the style your logo design should communicate.

```html
<!DOCTYPE html>
<html lang="en">
<head>
<meta charset="utf-8">
<title>Lomevu Business Card</title>
<link rel="stylesheet" href="https://fonts.googleapis.com/css2?family=Arimo:wght@400;700&display=swap">
<style>
  :root {
    --stage: #e9e6e1;
    --card-dark: #2e2f37;
    --card-grey: #bcbcbc;
    --brand-red: #c41f43;
    --text-light: #ffffff;
    --card-radius: 24px;
  }
  * { box-sizing: border-box; margin: 0; padding: 0; }
  html, body {
    width: 1200px;
    height: 798px;
    overflow: hidden;
    background: var(--stage);
    font-family: "Arimo", Arial, sans-serif;
  }
  .stage {
    position: relative;
    width: 1200px;
    height: 798px;
    display: flex;
    align-items: center;
    justify-content: center;
    gap: 60px;
  }
  .card {
    position: relative;
    width: 520px;
    height: 308px;
    border-radius: var(--card-radius);
    overflow: hidden;
    box-shadow: 0 10px 24px rgba(0, 0, 0, 0.25);
  }

  /* Front side */
  .card--front {
    background: var(--card-dark);
    display: flex;
    flex-direction: column;
    align-items: center;
    justify-content: center;
  }
  .brand {
    display: flex;
    align-items: center;
    gap: 16px;
    color: var(--brand-red);
    font-weight: 700;
    letter-spacing: 1px;
  }
  .brand__square {
    display: block;
    background: var(--brand-red);
    border-radius: 12px;
  }
  .card--front .brand { font-size: 44px; margin-top: -20px; }
  .card--front .brand__square { width: 48px; height: 48px; }
  .front__web {
    position: absolute;
    left: 0;
    right: 0;
    bottom: 12px;
    text-align: center;
    color: var(--text-light);
    font-size: 17px;
    letter-spacing: 6px;
  }

  /* Back side */
  .card--back {
    display: flex;
    background: var(--card-dark);
  }
  .back__logo-panel {
    position: relative;
    width: 50%;
    height: 100%;
    background: var(--card-grey);
    display: flex;
    align-items: center;
    justify-content: center;
  }
  .back__notch {
    position: absolute;
    right: 0;
    top: 34px;
    width: 0;
    height: 0;
    border-top: 9px solid transparent;
    border-bottom: 9px solid transparent;
    border-right: 12px solid var(--card-dark);
  }
  .card--back .brand { font-size: 30px; }
  .card--back .brand__square { width: 34px; height: 34px; border-radius: 9px; }
  .back__details {
    width: 50%;
    padding: 34px 0 0 28px;
    color: var(--text-light);
    font-size: 14px;
    line-height: 1.3;
  }
  .back__name {
    font-weight: 700;
    font-size: 15px;
    margin-bottom: 10px;
  }
  .back__details p { margin: 0; }
</style>
</head>
<body>
  <main class="stage">
    <section class="card card--front" aria-label="Card front">
      <div class="brand">
        <span class="brand__square"></span>
        <span class="brand__name">Lomevu</span>
      </div>
      <p class="front__web">www.lomevu-linkup.example</p>
    </section>

    <section class="card card--back" aria-label="Card back">
      <div class="back__logo-panel">
        <div class="brand">
          <span class="brand__square"></span>
          <span class="brand__name">Lomevu</span>
        </div>
        <span class="back__notch"></span>
      </div>
      <div class="back__details">
        <p class="back__name">Tobin Wexmoor</p>
        <p>+468213579 (singapore)</p>
        <p>+315792846 (Australia)</p>
        <p>+729384615 (America)</p>
        <p>www.lomevu-linkup.example</p>
        <p>ABN 86420913</p>
      </div>
    </section>
  </main>
</body>
</html>
```